YARD FRONTS "N" MORE

catyering to driveway/patio floor construction and remodeling. Concrete, concrete pavers, asphalt, Landscaping, irrigation, pergolas and pools.

Target Market(s)

the home owner that wants to enhance their home

Industry/Entity Type

construction

Contact Information for Business Card

presidet: tomas bellweather email: yardfrontsnmore@example.come office/cell: 555 214 8830

Font styles to use
Sans Serif

Requirements
Must have
• logo should pop out
Nice to have
• the logo should demonstrate that we do exteriors only

```html
<!DOCTYPE html>
<html lang="en">
<head>
<meta charset="utf-8">
<title>Yard Fronts "N" More – Business Card</title>
<link href="https://fonts.googleapis.com/css2?family=Oswald:wght@400;500;600&display=swap" rel="stylesheet">
<style>
  :root {
    --backdrop: #1d1e21;
    --concrete-light: #a9abac;
    --concrete-mid: #8d9092;
    --slate-light: #7a8688;
    --slate-dark: #4e5a5c;
    --grass-light: #3fa23a;
    --grass-dark: #1f6e22;
    --violet: #6462b8;
    --white: #ffffff;
    --soft-grey: #e4e4e4;
  }
  html, body {
    margin: 0;
    padding: 0;
    width: 1200px;
    height: 800px;
    overflow: hidden;
    background: var(--backdrop);
    font-family: "Oswald", sans-serif;
  }
  .canvas {
    position: relative;
    width: 1200px;
    height: 800px;
    display: flex;
    align-items: center;
    justify-content: center;
    gap: 40px;
  }
  .card {
    position: relative;
    width: 540px;
    height: 308px;
    border-radius: 18px;
    overflow: hidden;
    box-shadow: 0 10px 30px rgba(0,0,0,.45);
  }
  /* front */
  .card-front {
    background: linear-gradient(135deg, var(--slate-light), var(--slate-dark));
    display: flex;
    align-items: center;
    justify-content: center;
  }
  .brand-name {
    color: var(--white);
    font-weight: 600;
    text-transform: uppercase;
    letter-spacing: 1px;
    line-height: 1;
    margin: 0;
  }
  .card-front .brand-name { font-size: 40px; }
  /* back */
  .card-back {
    background: linear-gradient(135deg, var(--concrete-light), var(--concrete-mid));
  }
  .card-back svg.shapes {
    position: absolute;
    inset: 0;
  }
  .card-back .brand-name {
    position: absolute;
    left: 28px;
    top: 52px;
    font-size: 28px;
  }
  .service-list {
    position: absolute;
    right: 18px;
    top: 22px;
    margin: 0;
    padding: 0;
    list-style: none;
    text-align: right;
    color: var(--white);
    font-size: 11px;
    font-weight: 500;
    line-height: 15px;
    text-transform: uppercase;
  }
  .service-list li::after {
    content: "";
    display: inline-block;
    width: 5px;
    height: 5px;
    margin-left: 6px;
    background: var(--white);
    vertical-align: middle;
  }
  .contact {
    position: absolute;
    left: 34px;
    top: 168px;
    color: var(--white);
    text-transform: uppercase;
  }
  .contact-name { font-size: 22px; font-weight: 600; line-height: 1.1; }
  .contact-title { font-size: 15px; color: var(--soft-grey); line-height: 1.2; }
  .contact-phone {
    display: flex;
    align-items: center;
    gap: 8px;
    margin-top: 8px;
    font-size: 22px;
    font-weight: 500;
    line-height: 1;
  }
  .phone-icon {
    width: 22px; height: 22px;
    border-radius: 50%;
    background: var(--violet);
    display: flex; align-items: center; justify-content: center;
  }
  .contact-rule {
    width: 300px;
    height: 1px;
    background: var(--white);
    margin: 8px 0 6px;
  }
  .contact-email { font-size: 13px; text-transform: none; line-height: 1.3; }
  .contact-licence { font-size: 10px; color: var(--soft-grey); }
</style>
</head>
<body>
<main class="canvas">

  <section class="card card-front" role="img" aria-label="Concrete texture background with company name">
    <h1 class="brand-name">Yard Fronts "N" More</h1>
  </section>

  <section class="card card-back">
    <svg class="shapes" width="540" height="308" viewBox="0 0 540 308">
      <defs>
        <linearGradient id="grass" x1="0" y1="0" x2="1" y2="1">
          <stop offset="0" stop-color="var(--grass-light)"/>
          <stop offset="1" stop-color="var(--grass-dark)"/>
        </linearGradient>
      </defs>
      <path role="img" aria-label="Lawn grass texture band"
            d="M300,0 L540,0 L540,308 L370,308 C340,250 310,185 250,155 C175,122 85,125 0,165 L0,118 C95,82 210,82 300,0 Z"
            fill="url(#grass)"/>
      <path class="violet-swoosh" d="M0,172 C30,160 60,156 92,158 C55,170 25,195 0,240 Z" fill="var(--violet)"/>
      <circle class="badge" cx="430" cy="244" r="34" fill="#d9d9d9" stroke="var(--white)" stroke-width="4"/>
    </svg>

    <h2 class="brand-name">Yard Fronts "N" More</h2>

    <ul class="service-list">
      <li>Catyering to driveway/patio floor</li>
      <li>Construction and remodeling</li>
      <li>Concrete</li>
      <li>Concrete pavers</li>
      <li>Asphalt</li>
      <li>Landscaping</li>
      <li>Irrigation</li>
      <li>Pergolas and pools</li>
    </ul>

    <div class="contact">
      <div class="contact-name">Tomas Bellweather</div>
      <div class="contact-title">President</div>
      <div class="contact-phone">
        <span class="phone-icon">
          <svg width="12" height="12" viewBox="0 0 24 24"><path fill="#fff" d="M6.6 10.8a15.1 15.1 0 0 0 6.6 6.6l2.2-2.2a1 1 0 0 1 1-.25 11.4 11.4 0 0 0 3.6.57 1 1 0 0 1 1 1V20a1 1 0 0 1-1 1A17 17 0 0 1 3 4a1 1 0 0 1 1-1h3.5a1 1 0 0 1 1 1c0 1.25.2 2.45.57 3.57a1 1 0 0 1-.25 1Z"/></svg>
        </span>
        555 214 8830
      </div>
      <div class="contact-rule"></div>
      <div class="contact-email">yardfrontsnmore@example.come</div>
      <div class="contact-licence">Lic number : 98760421</div>
    </div>
  </section>

</main>
</body>
</html>
```